Lumira Book Cover for Teen Financial Niche

Had a temporary cover done for the book but it needs a lot better cover now it is starting to get some traction.
The current book can be seen here:
https://www.pelmarobooks.example/item/Q7H42ZR9KT
I am wanting something very different if possible. Please search books in the teen financial niche on Pelmaro and you will see that a lot of the covers are very similar in style.
I am looking for something different that will stand out in a crowded marketplace.
If you are putting someone on the cover please use a male character rather than a female one.
Thanks
Dale

```html
<!DOCTYPE html>
<html lang="en">
<head>
<meta charset="utf-8">
<title>Everyday Money Basics for Teens and Young Adults — Book Cover</title>
<link rel="stylesheet" href="https://fonts.googleapis.com/css2?family=Anton&family=Bebas+Neue&family=Oswald:wght@500;600&display=swap">
<style>
  :root {
    --denim-light: #2a4566;
    --denim-mid: #1b2f4a;
    --denim-dark: #0c1627;
    --cream: #ede4d4;
    --gold: #e9a23b;
    --red: #cf161c;
    --white: #ffffff;
  }
  html, body {
    margin: 0;
    padding: 0;
    width: 750px;
    height: 1200px;
    overflow: hidden;
    background: var(--denim-dark);
  }
  .cover {
    position: relative;
    width: 750px;
    height: 1200px;
    overflow: hidden;
  }
  .cover-backdrop {
    position: absolute;
    inset: 0;
    background:
      radial-gradient(ellipse at 35% 30%, var(--denim-light) 0%, transparent 60%),
      radial-gradient(ellipse at 60% 80%, #243b58 0%, transparent 55%),
      linear-gradient(160deg, var(--denim-mid) 0%, var(--denim-dark) 100%);
  }
  .author-name {
    position: absolute;
    left: 44px;
    top: 58px;
    margin: 0;
    font-family: "Oswald", sans-serif;
    font-weight: 600;
    font-size: 36px;
    line-height: 1;
    letter-spacing: 0.24em;
    color: var(--gold);
  }
  .title {
    margin: 0;
  }
  .title-line {
    position: absolute;
    left: 40px;
    display: block;
    font-family: "Anton", sans-serif;
    font-weight: 400;
    font-size: 160px;
    line-height: 1;
    letter-spacing: 0.01em;
    color: var(--cream);
    white-space: nowrap;
  }
  .title-line--first  { top: 376px; }
  .title-line--second { top: 544px; }
  .title-line--third  { top: 712px; }
  .audience-tag {
    position: absolute;
    left: 487px;
    top: 750px;
    width: 263px;
    height: 110px;
    box-sizing: border-box;
    padding-top: 13px;
    background: var(--red);
    color: var(--white);
    font-family: "Oswald", sans-serif;
    font-weight: 500;
    font-size: 35px;
    line-height: 42px;
    text-align: center;
  }
  .subtitle {
    position: absolute;
    left: 46px;
    top: 864px;
    margin: 0;
    font-family: "Bebas Neue", sans-serif;
    font-weight: 400;
    white-space: nowrap;
  }
  .subtitle-lead {
    display: block;
    font-size: 64px;
    line-height: 64px;
    color: var(--red);
  }
  .subtitle-detail {
    display: block;
    font-size: 44px;
    line-height: 60px;
    color: var(--cream);
  }
  .subtitle-accent {
    color: var(--gold);
  }
</style>
</head>
<body>
  <main class="cover">
    <div class="cover-backdrop" role="img" aria-label="Close-up photograph of dark blue denim jeans with a folded banknote tucked into the front pocket"></div>

    <p class="author-name">EZRA VALENTE</p>

    <h1 class="title">
      <span class="title-line title-line--first">EVERYDAY</span>
      <span class="title-line title-line--second">MONEY</span>
      <span class="title-line title-line--third">BASICS</span>
    </h1>

    <div class="audience-tag">FOR TEENS AND<br>YOUNG ADULTS</div>

    <h2 class="subtitle">
      <span class="subtitle-lead">CASH CONFIDENCE:</span>
      <span class="subtitle-detail"><span class="subtitle-accent">A GUIDE TO</span> EARNING MORE, BUDGETING SMART,</span>
      <span class="subtitle-detail">SPENDING WISELY, SAVING AND INVESTING</span>
    </h2>
  </main>
</body>
</html>
```